Briefpapierbogen-/Visitenkarten-Design für KFZ-Unternehmen
Zielgruppe
Wir sind ein junges /dynamisches Unternehmen das hochwertige Tuningartikel in Bereich KFZ verkauft bzw. vertreibt.
Unser Hauptaugenmerk liegt im Bereich Performance (Leistungssteigerungen) & Optik (Felgen, Fahrwerk)
Aufgabenstellung
Wir benötigen ein Briefpapierbogen sowie ein Visitenkarten Design!
Folgende Angaben müssen auf dem Briefpapier sein:
- Logo (siehe Anhang)
- Anschrift (KW Motorwerk UG (haftungsbeschränkt), Lindenhang 7, 99999 Musterdorf
- Wasserzeichen
- GF (Tobias Werlinger)
- Bankverbindung ( IBAN DE12 5501 0022 4417 3388 10, BIC HAVODEKKXXX)
-Steuernummer (52871/60432)
- Ust. ID (DE417293551)
- Telefon (+00 0000 - 4812306)
- FAX (+00 0000 - 6620417)
- email (info@kw-motorwerk.example)
- web (www.kw-motorwerk.example)
-shop (www.kwmot.example)
-fb kwmot.example
Folgende Angaben müssen auf der VK sein:

```html
<!DOCTYPE html>
<html lang="de">
<head>
<meta charset="utf-8">
<title>KW Motorwerk UG – Visitenkarte</title>
<link rel="stylesheet" href="https://fonts.googleapis.com/css2?family=Montserrat:wght@300;400;700&display=swap">
<style>
  :root {
    --paper: #ffffff;
    --card: #000000;
    --ink: #ffffff;
    --column-left: 265px;
    --column-width: 609px;
  }
  html, body {
    margin: 0;
    padding: 0;
    width: 1200px;
    height: 757px;
    overflow: hidden;
    background: var(--paper);
    font-family: "Montserrat", sans-serif;
  }
  .card {
    position: absolute;
    left: 30px;
    top: 28px;
    width: 1138px;
    height: 697px;
    background: var(--card);
    color: var(--ink);
    overflow: hidden;
  }
  .line {
    position: absolute;
    left: var(--column-left);
    width: var(--column-width);
    display: flex;
    justify-content: space-between;
    align-items: baseline;
    line-height: 1;
    white-space: nowrap;
    margin: 0;
  }
  .company-name {
    top: 90px;
    font-size: 61px;
    font-weight: 700;
    letter-spacing: -0.5px;
  }
  .legal-form {
    top: 153px;
    font-size: 15px;
    font-weight: 400;
    letter-spacing: 23.4px;
    width: calc(var(--column-width) + 24px);
  }
  .detail-large {
    font-size: 45px;
    font-weight: 300;
  }
  .detail-small {
    font-size: 23px;
    font-weight: 700;
    letter-spacing: 1.5px;
  }
  .address { top: 240px; font-size: 40px; }
  .manager { top: 297px; }
  .phone { top: 348px; font-size: 46px; letter-spacing: -1px; }
  .fax { top: 406px; }
  .email { top: 462px; font-size: 33px; }
  .web { top: 513px; }
  .shop { top: 560px; }
  .brand-mark {
    position: absolute;
    left: 955px;
    top: 600px;
    font-size: 62px;
    font-weight: 700;
    line-height: 1;
    color: var(--ink);
    margin: 0;
  }
</style>
</head>
<body>
  <main class="card">
    <h1 class="line company-name"><span>KW</span><span>Motorwerk</span><span>UG</span></h1>
    <p class="line legal-form"><span>(haftungsbeschränkt)</span></p>

    <p class="line detail-large address"><span>Lindenhang</span><span>7,</span><span>99999</span><span>Musterdorf</span></p>
    <p class="line detail-small manager"><span>GF</span><span>Tobias</span><span>Werlinger</span></p>
    <p class="line detail-large phone"><span>Telefon+00</span><span>0000</span><span>-</span><span>4812306</span></p>
    <p class="line detail-small fax"><span>FAX</span><span>+00</span><span>0000</span><span>-</span><span>6620417</span></p>
    <p class="line detail-large email"><span>email</span><span>info@kw-motorwerk.example</span></p>
    <p class="line detail-small web"><span>web</span><span>www.kw-motorwerk.example</span></p>
    <p class="line detail-large shop"><span>shop</span><span>www.kwmot.example</span></p>

    <p class="brand-mark">KW</p>
  </main>
</body>
</html>
```